Employee Handbook Cover

We need an cover for our employee handbook. The handbook should convey our core values of
-Family
-Accountability
-Professionalism
Attached is our logo. Please visit our website to get a feeling for what we do at www.kelmorvinco.com

```html
<!DOCTYPE html>
<html lang="en">
<head>
<meta charset="utf-8">
<title>Employee Handbook Cover</title>
<link rel="stylesheet" href="https://fonts.googleapis.com/css2?family=Cinzel:wght@600;700;800&family=Open+Sans:wght@700&display=swap">
<style>
  :root {
    --bg: #5e8f8c;
    --navy: #0e2a3c;
    --teal-dark: #0d2a33;
    --teal-mid: #17434a;
    --title-teal: #114a4a;
    --brand-blue: #2a3f9a;
    --cream-top: #fbfaf1;
    --cream-bottom: #eeeadb;
    --orange: #ef9c23;
    --orange-dark: #e38c17;
    --gold: #c9a93c;
    --tick: #f2c230;
    --white: #ffffff;
    --steel-light: #b9bcc6;
    --steel-dark: #1c1d24;
  }
  html, body {
    margin: 0;
    width: 1200px;
    height: 795px;
    overflow: hidden;
    background: var(--bg);
  }
  .cover {
    position: absolute;
    left: 330px;
    top: 27px;
    width: 540px;
    height: 740px;
    overflow: hidden;
    background: var(--cream-top);
    box-shadow: 0 8px 24px rgba(0,0,0,0.25);
  }
  .top-strip {
    position: absolute; left: 0; top: 0; width: 100%; height: 10px;
    background: var(--navy);
    border-bottom: 2px solid var(--white);
  }
  .title-area {
    position: absolute; left: 0; top: 12px; width: 100%; height: 236px;
    background: linear-gradient(180deg, var(--cream-top), var(--cream-bottom));
    text-align: center;
  }
  .brand {
    margin-top: 52px;
    display: inline-flex; align-items: center; gap: 10px;
    font-family: "Cinzel", serif; font-weight: 700; font-size: 26px;
    color: var(--brand-blue);
  }
  .brand-dot {
    width: 26px; height: 26px; border-radius: 50%;
    background: var(--brand-blue);
  }
  .doc-title {
    margin: 20px 0 0;
    font-family: "Cinzel", serif; font-weight: 800;
    color: var(--title-teal);
    line-height: 1;
  }
  .doc-title .line-1 { display: block; font-size: 40px; letter-spacing: 1px; }
  .doc-title .line-2 { display: block; font-size: 58px; letter-spacing: 1px; margin-top: 4px; }
  .author-band {
    position: absolute; left: 0; top: 248px; width: 100%; height: 52px;
    background: linear-gradient(180deg, var(--orange), var(--orange-dark));
    display: flex; align-items: center; justify-content: center;
  }
  .author-name {
    font-family: "Cinzel", serif; font-weight: 600; font-size: 17px;
    letter-spacing: 5px; color: var(--white);
  }
  .values-panel {
    position: absolute; left: 0; top: 300px; width: 100%; height: 196px;
    background: linear-gradient(90deg, var(--teal-dark), var(--teal-mid) 60%, var(--teal-dark));
  }
  .panel-frames { position: absolute; left: 0; top: 0; }
  .values-list {
    position: absolute; left: 130px; top: 48px;
    margin: 0; padding: 0; list-style: none;
    font-family: "Open Sans", sans-serif; font-weight: 700;
    font-size: 15px; letter-spacing: 2px; color: var(--white);
    line-height: 22px;
  }
  .values-list .tick { color: var(--tick); margin-right: 4px; }
  .gold-rule {
    position: absolute; left: 0; top: 496px; width: 100%; height: 4px;
    background: var(--gold);
  }
  .gears-photo {
    position: absolute; left: 0; top: 500px; width: 100%; height: 240px;
    background: radial-gradient(circle at 40% 55%, var(--steel-light) 0%, #7d808c 35%, #3a3c46 70%, var(--steel-dark) 100%);
  }
</style>
</head>
<body>
  <main class="cover">
    <div class="top-strip"></div>
    <header class="title-area">
      <div class="brand"><span class="brand-dot"></span>Kelmorvin</div>
      <h1 class="doc-title"><span class="line-1">EMPLOYEE</span><span class="line-2">HANDBOOK</span></h1>
    </header>
    <div class="author-band"><span class="author-name">AUTHOR NAME</span></div>
    <section class="values-panel">
      <svg class="panel-frames" width="540" height="196" viewBox="0 0 540 196" fill="none" stroke="var(--gold)" stroke-width="1.2">
        <rect x="350" y="14" width="110" height="80" rx="14"/>
        <rect x="345" y="70" width="80" height="60" rx="12"/>
        <rect x="400" y="100" width="45" height="38" rx="9"/>
        <rect x="25" y="70" width="70" height="52" rx="10"/>
        <rect x="20" y="110" width="50" height="40" rx="8"/>
        <rect x="58" y="128" width="30" height="26" rx="6"/>
      </svg>
      <ul class="values-list">
        <li><span class="tick">✓</span>FAMILY</li>
        <li><span class="tick">✓</span>ACCOUNTABILITY</li>
        <li><span class="tick">✓</span>PROFESSIONALISM</li>
      </ul>
    </section>
    <div class="gold-rule"></div>
    <div class="gears-photo" role="img" aria-label="Photograph of interlocking steel gears"></div>
  </main>
</body>
</html>
```